Zenith Grease street sign

looking for a fresh new looking street sign .. sized 6ft tall 5ft wide <br/>"Zenith Grease<br/>The Velocity Crew"<br/>remove "... and Tune"<br/>remove "Kravo" the bottom should just read "The Velocity Crew"

Target Market(s)

motorist passing my location

Industry/Entity Type

Automotive

Font styles to use
Sans Serif

Requirements
Must have
• Zenith Grease
• The Velocity Crew
Should not have
• NO reference to "Kravo"

```html
<!DOCTYPE html>
<html lang="en">
<head>
<meta charset="utf-8">
<title>Zenith Grease – Street Sign</title>
<link rel="stylesheet" href="https://fonts.googleapis.com/css2?family=Oswald:wght@700&display=swap">
<style>
  :root{
    --backdrop:#e9eef2;
    --panel-blue:#0b2a86;
    --panel-blue-deep:#061a5c;
    --frame-grey:#c6c8ca;
    --silver-light:#f4f4f4;
    --silver-mid:#a9abae;
    --silver-dark:#5e6064;
    --red-bright:#e3222a;
    --red-deep:#8e0710;
    --ink:#1a1414;
    --white:#ffffff;
  }
  html,body{margin:0;padding:0;width:1200px;height:750px;overflow:hidden;background:var(--backdrop);}
  .sign-canvas{display:block;width:1200px;height:750px;}
  .brand-name{font-family:"Oswald",sans-serif;font-weight:700;font-size:96px;fill:var(--white);text-anchor:middle;}
  .tagline{font-family:"Oswald",sans-serif;font-weight:700;font-size:34px;fill:url(#silverText);stroke:var(--ink);stroke-width:1.5px;paint-order:stroke;text-anchor:middle;}
  .flag-area{fill:url(#flagTones);}
  .panel{fill:url(#panelBlue);}
  .frame-plain{fill:var(--frame-grey);}
  .frame-metal{fill:url(#silverBand);}
  .trim-line{fill:none;stroke:var(--red-bright);stroke-width:2;}
  .stop-red-bright{stop-color:var(--red-bright);}
  .stop-red-deep{stop-color:var(--red-deep);}
  .stop-silver-light{stop-color:var(--silver-light);}
  .stop-silver-mid{stop-color:var(--silver-mid);}
  .stop-silver-dark{stop-color:var(--silver-dark);}
  .stop-blue{stop-color:var(--panel-blue);}
  .stop-blue-deep{stop-color:var(--panel-blue-deep);}
</style>
</head>
<body>
<svg class="sign-canvas" viewBox="0 0 1200 750" xmlns="http://www.w3.org/2000/svg">
  <defs>
    <linearGradient id="silverText" x1="0" y1="0" x2="0" y2="1">
      <stop offset="0" class="stop-silver-light"/>
      <stop offset="0.5" class="stop-silver-mid"/>
      <stop offset="1" class="stop-silver-light"/>
    </linearGradient>
    <linearGradient id="silverBand" x1="0" y1="0" x2="1" y2="0">
      <stop offset="0" class="stop-silver-mid"/>
      <stop offset="0.3" class="stop-silver-light"/>
      <stop offset="0.6" class="stop-silver-dark"/>
      <stop offset="1" class="stop-silver-light"/>
    </linearGradient>
    <radialGradient id="panelBlue" cx="0.5" cy="0.45" r="0.7">
      <stop offset="0" class="stop-blue"/>
      <stop offset="1" class="stop-blue-deep"/>
    </radialGradient>
    <linearGradient id="flagTones" x1="0" y1="0" x2="1" y2="1">
      <stop offset="0" class="stop-silver-light"/>
      <stop offset="0.5" class="stop-silver-dark"/>
      <stop offset="1" class="stop-silver-light"/>
    </linearGradient>
    <linearGradient id="pillRed" x1="0" y1="0" x2="0" y2="1">
      <stop offset="0" class="stop-red-bright"/>
      <stop offset="1" class="stop-red-deep"/>
    </linearGradient>
  </defs>

  <!-- Sign A: grey frame with red tagline plate -->
  <g class="sign sign--plate">
    <rect class="frame-plain" x="113" y="117" width="450" height="538"/>
    <rect class="panel" x="122" y="126" width="433" height="521"/>
    <rect class="flag-area" role="img" aria-label="Two crossed chequered racing flags" x="172" y="150" width="340" height="145" rx="30" opacity="0.85"/>

    <text class="brand-name" x="338" y="392">Zenith</text>
    <text class="brand-name" x="338" y="492">Grease</text>

    <rect x="147" y="524" width="382" height="81" rx="14" fill="url(#silverBand)"/>
    <rect x="158" y="533" width="360" height="63" rx="10" fill="url(#pillRed)" stroke="var(--white)" stroke-width="2"/>
    <text class="tagline" x="338" y="580">The Velocity Crew</text>
  </g>

  <!-- Sign B: brushed-metal frame with notched bands -->
  <g class="sign sign--metal">
    <rect class="frame-metal" x="643" y="121" width="442" height="530"/>
    <rect class="panel" x="651" y="150" width="426" height="470"/>

    <path class="frame-metal" d="M643 121H1085V150H955L935 168H792L772 150H643Z"/>
    <path class="trim-line" d="M643 142H770L790 159H937L957 142H1085"/>
    <path class="frame-metal" d="M643 651H1085V605H958L940 620H788L770 605H643Z"/>
    <path class="trim-line" d="M643 613H768L786 628H942L960 613H1085"/>

    <rect class="flag-area" role="img" aria-label="Two crossed chequered racing flags" x="697" y="193" width="342" height="145" rx="30" opacity="0.85"/>

    <text class="brand-name" x="864" y="432">Zenith</text>
    <text class="brand-name" x="864" y="528">Grease</text>

    <text class="tagline" x="864" y="582">The Velocity Crew</text>
  </g>
</svg>
</body>
</html>
```